Gutschein-Design für Apotheken
Zielgruppe
Unsere Familie betreibt 4 Apotheken in Bayern.
Diese haben seit kurzem die Dachmarke und dem CI 'Lerchen-Apotheken', sind aber alle weiter unter eigenem Namen eigenständig.
Unsere Kunden erhalten als Dankeschön für den Besuch einen netten Prämienlerche, der dann gegen schöne Dinge eingetauscht werden kann.
Wir suchen einen neuen Gutschein für unsere Kunden, der in allen Apotheken von uns erworben werden kann und auch überall eingelöst werden kann.
Bisher hatte jede Apotheke einzelne Gutscheine. Die Apotheke Am Lindenhof hat zusätzlich noch einen reinen Kosmetikgutschein, der für Behandlungen etc. ausgegeben wird.
Nun suchen wir einen neuen Gutschein, in dem der Barwert (z.B. 40€) eingetragen wird und der für alles (Arzneimittel, Bonbons etc.) und überall eingelöst werden kann.
Ziel: gemeinsamer Gutschein für Kunden
Format: bevorzugt wie Kosmetikgutschein, gerne aber auch andere Ideen erwünscht (Gutscheinkarte in dem Format, dafür hinten und vorne Info?)
BITTE MODERNES DESIGN, kein klassisches, altbackenes Design von Apotheken (Blümchen etc.)
Inhalt: nicht wirklich viel:
- Gutschein über
- Leerzeichen wo Betrag eingetragen wird
- Gutscheinnummer; Leerzeichen, wo Nummer eingetragen wird
- Datum Unterschrift
- Information, dass dieser Gutschein in allen unseren Apotheken eingelöst werden kann.
- keine Gültigkeit! (Kunden können den Gutschein unendlich lang einlösen bei uns)
- irgend ein netter Spruch? 'Gesundheit ist alles' o.ä 'Gesundheit schenken'... ?!
- evtl. nettes Bild / Gesundheit etc.
- Logos und Adressen von allen 4 Apotheken
- GERNE Lerche mit einbauen (ist unser Wiedererkennungswert! )
(Achtung: 3x Wendtaler Apotheken haben einen technischen Lerche, Apotheke Rodenau hat einen anderen. Ist aber ok so!)
Anbei Beispiele von Flyern, wo wir halbprofessionell schon alle 4 Apotheken mit auf den Flyer tun.
An..
Aufgabenstellung
siehe Anhang

```html
<!DOCTYPE html>
<html lang="de">
<head>
<meta charset="utf-8">
<title>Gutschein – Lerchen-Apotheken</title>
<link rel="stylesheet" href="https://fonts.googleapis.com/css2?family=Didact+Gothic&family=Cabin:wght@400;600&display=swap">
<style>
  :root{
    --navy:#1f2346;
    --magenta:#f21fce;
    --ribbon:#cf5fd6;
    --field:#c4c4c8;
    --ink:#1a1a1a;
    --red:#d8141b;
    --stage:#d9d9db;
    --white:#ffffff;
  }
  *{box-sizing:border-box;margin:0;padding:0}
  html,body{width:1200px;height:676px;overflow:hidden;background:var(--stage)}
  .canvas{position:relative;width:1200px;height:676px}
  .card{position:absolute;left:62px;width:1076px;height:251px;overflow:hidden;background:var(--white)}
  .card--front{top:42px}
  .card--back{top:399px}

  .crystal-art{position:absolute;inset:0}
  .card--front .crystal-art{
    background:
      radial-gradient(ellipse 30% 70% at 52% 45%, rgba(250,110,150,.95), rgba(250,110,150,0) 70%),
      radial-gradient(ellipse 22% 40% at 55% 18%, rgba(255,150,80,.85), rgba(255,150,80,0) 70%),
      radial-gradient(ellipse 25% 60% at 8% 70%, rgba(120,180,235,.9), rgba(120,180,235,0) 75%),
      radial-gradient(ellipse 22% 60% at 96% 60%, rgba(140,195,240,.85), rgba(140,195,240,0) 75%),
      radial-gradient(ellipse 30% 40% at 30% 90%, rgba(190,140,220,.7), rgba(190,140,220,0) 75%),
      linear-gradient(180deg,#fbf8fb 0%,#f4e9f3 60%,#e6d6ee 100%);
  }
  .card--back .crystal-art{
    background:
      radial-gradient(ellipse 14% 75% at 0% 60%, rgba(130,190,235,.75), rgba(130,190,235,0) 80%),
      radial-gradient(ellipse 10% 70% at 100% 50%, rgba(130,195,240,.75), rgba(130,195,240,0) 80%),
      radial-gradient(ellipse 30% 50% at 30% 25%, rgba(245,190,225,.35), rgba(245,190,225,0) 75%),
      radial-gradient(ellipse 40% 30% at 50% 100%, rgba(200,215,245,.5), rgba(200,215,245,0) 75%),
      #ffffff;
  }

  .ribbon{position:absolute;height:5px;background:var(--ribbon);transform-origin:left center}
  .card--front .ribbon{left:820px;top:-2px;width:470px;transform:rotate(19deg)}
  .card--back .ribbon{left:955px;top:-2px;width:160px;transform:rotate(24deg)}
  .bow{position:absolute;border-radius:40%;background:radial-gradient(circle,#e493e6,#c148c9)}
  .card--front .bow{left:920px;top:12px;width:100px;height:80px}
  .card--back .bow{left:1000px;top:8px;width:50px;height:36px}
  .lark-dot{position:absolute;width:12px;height:12px;border-radius:50%;background:var(--red)}
  .card--front .lark-dot{left:1049px;top:13px}
  .card--back .lark-dot{left:964px;top:58px}

  .display{font-family:"Didact Gothic",sans-serif;position:absolute;white-space:nowrap;line-height:1}
  .headline-kicker{left:650px;top:102px;font-size:45px;color:var(--navy);letter-spacing:3px}
  .headline-main{left:582px;top:150px;font-size:96px;color:var(--magenta);letter-spacing:3px;
    -webkit-text-stroke:2px var(--white);paint-order:stroke fill}
  .claim{left:24px;top:207px;font-size:25px;color:var(--white);letter-spacing:2px}

  .form-row{position:absolute;left:632px;display:flex;align-items:center;height:29px}
  .form-label{width:132px;font-family:"Didact Gothic",sans-serif;font-size:12px;letter-spacing:1px;color:var(--navy)}
  .form-label small{font-family:"Cabin",sans-serif;font-size:10px;letter-spacing:0}
  .form-field{width:213px;height:29px;background:var(--field)}
  .row-value{top:64px}
  .row-number{top:114px}
  .row-date{top:161px}

  .validity{position:absolute;left:71px;top:149px;font-family:"Cabin",sans-serif;font-size:10px;color:var(--navy)}
  .branches{position:absolute;left:71px;top:168px;display:flex;gap:12px;align-items:flex-start}
  .branch{font-family:"Cabin",sans-serif;color:var(--ink);line-height:1.25}
  .branch-name{font-family:"Cabin",sans-serif;font-weight:600;font-size:10px;display:flex;align-items:center;gap:4px;
    border-bottom:1px solid var(--ink);padding-bottom:2px;margin-bottom:3px;white-space:nowrap}
  .branch-name::before{content:"";width:7px;height:7px;border-radius:50%;background:var(--red);flex:none}
  .branch-line{font-size:5.5px;white-space:nowrap}
  .branch-line--big{font-size:8px}
  .branch-new{font-size:6px;color:var(--red);font-weight:600}
  .branch--lindenhof{width:90px}
  .branch--markt{width:102px}
  .branch--rodenau{width:100px}
  .branch--vitaplus{width:80px}
</style>
</head>
<body>
<main class="canvas">

  <section class="card card--front" aria-label="Gutschein Vorderseite">
    <div class="crystal-art" role="img" aria-label="Polygonales Kristallmuster in Rosa, Orange und Hellblau"></div>
    <div class="ribbon"></div>
    <div class="bow" role="img" aria-label="Rosa Geschenkschleife"></div>
    <span class="lark-dot"></span>
    <p class="display headline-kicker">Der zeitlose</p>
    <h1 class="display headline-main">Gutschein</h1>
    <p class="display claim">Ihre Gesundheit liegt uns am Herzen.</p>
  </section>

  <section class="card card--back" aria-label="Gutschein Rückseite">
    <div class="crystal-art" role="img" aria-label="Zartes polygonales Kristallmuster in Pastelltönen"></div>
    <div class="ribbon"></div>
    <div class="bow" role="img" aria-label="Rosa Geschenkschleife"></div>

    <div class="form-row row-value"><span class="form-label">Gutschein in <small>Höhe von:</small></span><span class="form-field"></span></div>
    <div class="form-row row-number"><span class="form-label">Gutscheinnummer:</span><span class="form-field"></span></div>
    <div class="form-row row-date"><span class="form-label">Datum, <small>Unterschrift:</small></span><span class="form-field"></span></div>
    <span class="lark-dot"></span>

    <p class="validity">Gültig in allen Apotheken mit der Lerche.</p>

    <div class="branches">
      <div class="branch branch--lindenhof">
        <p class="branch-name">Am Lindenhof</p>
        <p class="branch-line branch-line--big">LINDENSTRASSE 6</p>
        <p class="branch-line branch-line--big">TEL: 01234 / 5678-0</p>
        <p class="branch-line branch-line--big">FAX: 01234 / 5678-20</p>
        <p class="branch-line">lindenhof@lerchen-apotheken.de</p>
      </div>
      <div class="branch branch--markt">
        <p class="branch-name">MARKT-APOTHEKE</p>
        <p class="branch-line">Am Marktplatz 1 &nbsp; 91234 Wendtal</p>
        <p class="branch-line">Tel: 01234 / 44120 &nbsp; Fax: 01234 / 44129</p>
        <p class="branch-line">markt@lerchen-apotheken.de</p>
      </div>
      <div class="branch branch--rodenau">
        <p class="branch-name">APOTHEKE RODENAU</p>
        <p class="branch-line">Kirchgasse 1 &nbsp; Rodenau</p>
        <p class="branch-line">Tel: 05678 / 3310-0 &nbsp; Fax: 05678 / 3310-20</p>
        <p class="branch-line">rodenau@lerchen-apotheken.de</p>
      </div>
      <div class="branch branch--vitaplus">
        <p class="branch-name">vitaplus apotheke</p>
        <p class="branch-line">Werkstraße 15 &nbsp; 91234 Wendtal</p>
        <p class="branch-line">vitaplus@lerchen-apotheken.de</p>
        <p class="branch-new">NEU! Ab Januar 2018</p>
      </div>
    </div>
  </section>

</main>
</body>
</html>
```